Welcome Brochure for new visitors to our church

We are a lively family church and need a brochure to give out to people when they first come to our church providing them with info about who we are and what we're about. We would like the brochures theme to fit with our vibrant logo with pictures (we may need to provide some?) It would be good to include some of our logos (attached) The attached file is only a basic format so making the information look fun would be great, so outlining the ministries for example in a more interesting way, rather than just a list. The general order of the text would be good to keep, but also the CONNECT, ENGAGE, GROW and GO could be presented in a more exciting way? I've selected the colours , but not sure if they're the exact ones from the logo, and can't seem to upload the logo as it's too wide, but have included it in the word doc.

Target Market(s)

Families

Industry/Entity Type

Church

Other font styles liked:
• Lato

Colors
e34297
a54499
6b449b
0355a3
85cae6

Requirements
Must have
• Colourful and easy to read

```html
<!DOCTYPE html>
<html lang="en">
<head>
<meta charset="utf-8">
<title>Bright Path Church – Welcome Pack</title>
<link rel="stylesheet" href="https://fonts.googleapis.com/css2?family=Lato:wght@400;700;900&display=swap">
<style>
:root{
  --pink:#e34297;
  --purple:#a54499;
  --violet:#6b449b;
  --blue:#0355a3;
  --sky:#85cae6;
  --lilac:#efe6f3;
  --ink:#3b3b45;
  --stage:#e8e8ec;
  --paper:#ffffff;
}
*{margin:0;padding:0;box-sizing:border-box}
html,body{width:1200px;height:4500px;overflow:hidden}
body{background:var(--stage);font-family:'Lato',Arial,sans-serif;color:var(--ink);position:relative}
.page{position:absolute;background:var(--paper);overflow:hidden;box-shadow:0 2px 10px rgba(0,0,0,.12)}
.photo{position:absolute}
.wave{position:absolute;left:0;width:100%}
.body-copy{position:absolute;font-size:11.5px;line-height:1.55}
.body-copy p{margin-bottom:9px}

/* cover */
.cover{left:320px;top:50px;width:560px;height:790px}
.cover .photo{left:0;top:0;width:560px;height:600px;background:linear-gradient(160deg,#c9b27a 0%,#a99a63 35%,#7e8452 65%,#5e6a3f 100%)}
.cover-brand{position:absolute;left:300px;top:42px;display:flex;align-items:center;gap:8px;font-weight:900;font-size:17px;color:var(--pink)}
.cover-brand .dot{width:16px;height:16px;border-radius:50%;background:var(--pink)}
.cover-title{position:absolute;left:250px;top:74px;font-weight:900;font-size:52px;letter-spacing:2px;line-height:1;background:linear-gradient(90deg,var(--pink),var(--violet),var(--blue));-webkit-background-clip:text;background-clip:text;color:transparent}
.cover-web{position:absolute;left:40px;top:744px;font-size:13px;font-weight:700;letter-spacing:2px;color:#fff;text-transform:uppercase}

/* spreads */
.spread{position:absolute;left:60px;width:1080px;height:760px}
.spread .page{top:0;width:540px;height:760px}
.spread .left{left:0}
.spread .right{left:540px}
.head-band{position:absolute;left:0;top:34px;height:52px;width:330px;background:var(--lilac);border-radius:0 26px 26px 0;border-left:8px solid var(--sky)}
.head-band .knob{position:absolute;left:6px;top:9px;width:34px;height:34px;border-radius:50%;background:var(--violet)}
.head-band h2{position:absolute;left:52px;top:14px;font-size:20px;font-weight:900;color:var(--violet);white-space:nowrap}
.head-band.alt .knob{background:var(--purple)}
.head-band.alt{border-left-color:var(--pink)}
.head-band.blue h2{color:var(--blue)}
.head-band.blue .knob{background:var(--blue)}

.welcome-title{position:absolute;left:40px;top:30px;font-weight:900;font-size:26px;line-height:1.15;color:var(--purple)}
.welcome-title span{color:var(--blue)}
.brand-mark{position:absolute;display:flex;align-items:center;gap:6px;font-weight:900;font-size:13px;color:var(--purple)}
.brand-mark .dot{width:12px;height:12px;border-radius:50%;background:var(--purple)}
.sign{font-style:normal;font-weight:700;color:var(--violet)}

.family-photo{left:48px;top:120px;width:444px;height:360px;border-radius:26px;background:linear-gradient(150deg,#f1e8e4,#c7b7b2 55%,#8d7f86)}
.caption{position:absolute;left:60px;top:600px;color:#fff;font-weight:900;font-size:21px;line-height:1.25}

.aims{position:absolute;left:40px;top:390px;width:440px}
.aim{display:flex;gap:14px;margin-bottom:16px;align-items:flex-start}
.aim svg{flex:0 0 40px}
.aim h3{font-size:13px;font-weight:900;color:var(--violet);letter-spacing:1px}
.aim p{font-size:10.5px;line-height:1.45}

.group-photo{left:0;top:430px;width:540px;height:270px;background:linear-gradient(180deg,#f4c98a 0%,#e7a35a 45%,#7c5a3a 100%)}
.path-photo{left:0;top:470px;width:540px;height:290px;background:linear-gradient(180deg,#cfd3d6,#9ea4a8 55%,#6d7276)}
.strip{position:absolute;left:40px;top:300px;width:460px;height:70px;display:flex;gap:6px;padding:6px;background:var(--sky);border-radius:8px}
.strip div{flex:1;border-radius:4px;background:linear-gradient(160deg,#7fa2c4,#36557c)}
.ministries{position:absolute;left:40px;top:390px;width:460px;display:grid;grid-template-columns:1fr 1fr;gap:4px 20px;list-style:none;font-size:11px;font-weight:700;color:var(--blue)}
.ministries li{display:flex;align-items:center;gap:7px}
.ministries li::before{content:"";width:7px;height:7px;border-radius:50%;background:var(--purple)}

/* letter */
.letter{left:230px;top:3390px;width:740px;height:1046px;background:#fffdf8}
.letter h2{position:absolute;left:0;width:100%;top:70px;text-align:center;font-weight:900;font-size:32px;letter-spacing:2px;color:var(--purple)}
.letter h2 span{color:var(--pink)}
.letter .body-copy{left:70px;top:150px;width:600px;font-size:13px}
.form{position:absolute;left:70px;top:480px;width:600px;border:2px solid var(--sky);border-radius:14px;padding:24px 28px}
.form h3{font-size:15px;font-weight:900;color:var(--blue);margin-bottom:14px}
.field{display:flex;gap:12px;align-items:flex-end;margin-bottom:16px;font-size:12px;font-weight:700;color:var(--violet)}
.field span{flex:0 0 120px}
.field i{flex:1;border-bottom:1px solid #b9b0c4;height:16px}
.checks{display:flex;gap:26px;font-size:12px;margin-top:6px}
.checks label{display:flex;gap:8px;align-items:center}
.checks b{width:14px;height:14px;border:1.5px solid var(--purple);border-radius:3px;display:inline-block}
</style>
</head>
<body>

<!-- COVER -->
<section class="page cover">
  <div class="photo" role="img" aria-label="Photograph of a group of smiling friends embracing outdoors in golden sunlight"></div>
  <svg class="wave" style="top:480px" width="560" height="310" viewBox="0 0 560 310" aria-hidden="true">
    <path d="M0 90 C150 20 330 150 560 60 L560 310 L0 310Z" fill="#fff"/>
    <path d="M0 210 C160 170 340 250 560 190 L560 310 L0 310Z" fill="var(--sky)"/>
    <path d="M0 245 C170 215 360 285 560 235 L560 310 L0 310Z" fill="var(--blue)"/>
  </svg>
  <div class="cover-brand"><span class="dot"></span>Bright Path Church</div>
  <h1 class="cover-title">WELCOME<br>PACK</h1>
  <div class="cover-web">www.brightpathchurch.org</div>
</section>

<!-- SPREAD 1 -->
<section class="spread" style="top:910px">
  <article class="page left">
    <svg class="wave" style="top:0" width="540" height="130" viewBox="0 0 540 130" aria-hidden="true">
      <path d="M0 0 H380 C340 60 260 110 0 118Z" fill="var(--lilac)"/>
      <path d="M0 0 H40 V118 H0Z" fill="var(--purple)"/>
    </svg>
    <h1 class="welcome-title" style="left:56px">WELCOME <span>TO</span><br><span>BRIGHT PATH CHURCH NR4!</span></h1>
    <div class="brand-mark" style="left:400px;top:44px"><span class="dot"></span>Bright Path</div>
    <div class="body-copy" style="left:56px;top:160px;width:430px">
      <p>We are so pleased you have decided to join us for the service today; we really appreciate you taking time out of your schedule to be with us.</p>
      <p>You deciding to be with us is something we never take for granted and I hope you enjoy your visit to Bright Path Church.</p>
      <p>Bright Path Church is part of the Harbour denomination and has churches all around the UK and the World. If you would like find out more about Harbour and the work it does please go to www.harbourchurches.org to find out more.</p>
      <p>This pack is designed to explain a little about who we are and what we do. If you have any further questions or queries please do not hesitate in making contact with us where one of the team will contact you.</p>
      <p>If there is one thing we encourage everyone to be at Bright Path Church is to be yourself; we are all on a journey and today this could be the start of your journey with us. We hope to see you again at one of our services or events in the near future.</p>
      <p>All the best,<br><em class="sign">Daniel</em></p>
    </div>
    <svg class="wave" style="bottom:0" width="540" height="110" viewBox="0 0 540 110" aria-hidden="true">
      <path d="M0 40 C160 110 340 0 540 50 L540 110 L0 110Z" fill="var(--purple)"/>
      <path d="M0 80 C180 120 360 50 540 85 L540 110 L0 110Z" fill="var(--blue)"/>
    </svg>
  </article>
  <article class="page right" style="background:var(--violet)">
    <svg class="wave" style="top:0" width="540" height="760" viewBox="0 0 540 760" aria-hidden="true">
      <path d="M0 0 H540 V40 C420 80 300 40 200 90 C120 130 40 120 0 100Z" fill="var(--purple)"/>
      <path d="M0 100 C60 80 140 130 220 100 C330 60 430 90 540 70 V560 C420 520 300 600 0 540Z" fill="#fff"/>
      <path d="M0 540 C250 610 380 500 540 560 V760 H0Z" fill="var(--blue)"/>
    </svg>
    <div class="photo family-photo" role="img" aria-label="Photograph of the senior minister with his wife and young son"></div>
    <div class="caption">Senior Minister Daniel Marsh<br>and his wife Hannah and son Toby</div>
  </article>
</section>

<!-- SPREAD 2 -->
<section class="spread" style="top:1730px">
  <article class="page left">
    <div class="head-band"><span class="knob"></span><h2>THE BRIGHT PATH AIM &amp; VISION</h2></div>
    <div class="body-copy" style="left:40px;top:112px;width:460px">
      <p>At Bright Path Church we like to keep things as simple as possible. In light of that, what we are trying to be and achieve is pretty simple.</p>
      <p>Our aim and vision is to be a church where people can connect, engage, grow &amp; go.</p>
      <p>We believe Jesus is still active and present in the world today, and we are trying to live our lives to be like Him in all we do.</p>
      <p>As a church our aims are:</p>
    </div>
    <div class="aims" style="top:290px">
      <div class="aim">
        <svg width="40" height="40" viewBox="0 0 40 40" aria-hidden="true"><circle cx="20" cy="20" r="19" fill="var(--violet)"/><circle cx="15" cy="20" r="6" fill="none" stroke="#fff" stroke-width="2.5"/><circle cx="25" cy="20" r="6" fill="none" stroke="#fff" stroke-width="2.5"/></svg>
        <div><h3>CONNECT</h3><p>as a Church family meeting as much as possible, learning about living life for Jesus.</p></div>
      </div>
      <div class="aim">
        <svg width="40" height="40" viewBox="0 0 40 40" aria-hidden="true"><circle cx="20" cy="20" r="19" fill="var(--purple)"/><path d="M20 29 L11 20 A5 5 0 0 1 20 13 A5 5 0 0 1 29 20Z" fill="#fff"/></svg>
        <div><h3>ENGAGE</h3><p>getting involved in church life as much as possible as we love being part of an amazing team for Jesus.</p></div>
      </div>
      <div class="aim">
        <svg width="40" height="40" viewBox="0 0 40 40" aria-hidden="true"><circle cx="20" cy="20" r="19" fill="var(--pink)"/><path d="M20 29 V12 M13 18 L20 11 L27 18" fill="none" stroke="#fff" stroke-width="3" stroke-linecap="round"/></svg>
        <div><h3>GROW</h3><p>quite simply, we want our relationship with Jesus to grow and get stronger as we do life!</p></div>
      </div>
      <div class="aim">
        <svg width="40" height="40" viewBox="0 0 40 40" aria-hidden="true"><circle cx="20" cy="20" r="19" fill="var(--blue)"/><path d="M11 20 H28 M22 13 L29 20 L22 27" fill="none" stroke="#fff" stroke-width="3" stroke-linecap="round"/></svg>
        <div><h3>GO</h3><p>We want to tell others about how amazing the God we follow is! If this sounds like something you'd like to find out more about please let us know!</p></div>
      </div>
    </div>
    <svg class="wave" style="bottom:0" width="540" height="90" viewBox="0 0 540 90" aria-hidden="true">
      <path d="M0 30 C180 90 360 0 540 40 L540 90 L0 90Z" fill="var(--sky)"/>
      <path d="M0 60 C200 100 360 40 540 70 L540 90 L0 90Z" fill="var(--purple)"/>
    </svg>
  </article>
  <article class="page right">
    <div class="head-band blue"><span class="knob"></span><h2>CONNECT GROUPS</h2></div>
    <div class="body-copy" style="left:40px;top:112px;width:460px">
      <p>One of our first and main aims is 'Connect'. Bright Path Church is a family orientated church and we want to connect with each other as much as possible. When we keep connecting we can continually find out how others are doing. When we know this it allows us to support and care for each other as best as we can.</p>
      <p>We connect on a Sunday when we gather to worship and we actively encourage everyone who counts Bright Path as their home church to be in a Connect Group (CG) as much as possible.</p>
      <p>Our CG's meet on a regular basis and are a great way to make deeper friendships, be in a support group, go deeper in God's Word and have fun!</p>
      <p>Bright Path Church is a gathered church which means although we meet as a church in Millbrook many people in the church travel from all around the area from places such as Ashford Vale, Kingsmere and Oakley to name a few. In light of this we have CG's currently running in Millbrook and Oakley. If you decide to be part of Bright Path Church and would like to be part of a CG, please let us know.</p>
    </div>
    <div class="photo group-photo" style="top:480px;height:280px" role="img" aria-label="Photograph of friends standing arm in arm watching a sunset"></div>
  </article>
</section>

<!-- SPREAD 3 -->
<section class="spread" style="top:2550px">
  <article class="page left">
    <div class="head-band alt"><span class="knob"></span><h2>BEING PART OF THE FAMILY</h2></div>
    <div class="body-copy" style="left:40px;top:112px;width:460px">
      <p>For anyone considering joining a church this can be quite a daunting challenge at times and we never want anyone to feel under pressure at Bright Path Church. If and when someone decides they would like to be part of the Bright Path family then, after a period of time of regularly being with us (around six months), we'd encourage anyone who is interested to consider becoming a member of the church.</p>
      <p>This would involve a discussion with the minister and attending a course (one or two evenings) to go through the membership booklet, but of all the things membership does it says the person wishing to become a member wants to be fully 'part' of the family.</p>
      <p>Membership is an amazing way of finding you are really joining in the journey of where God is leading and taking Bright Path Church.</p>
      <p>If you decide that Bright Path Church is the place for you then after a few months if you are interested in finding out more about membership please speak to Daniel or Hannah for further details.</p>
    </div>
    <div class="photo path-photo" role="img" aria-label="Photograph of two people walking hand in hand along a rocky mountain path"></div>
  </article>
  <article class="page right">
    <div class="head-band blue"><span class="knob"></span><h2>BRIGHT PATH MINISTRIES</h2></div>
    <div class="body-copy" style="left:40px;top:112px;width:460px">
      <p>Quite simply Bright Path Church could not do all it does and wants to achieve in the future without the amazing group of volunteers who make things happen.</p>
      <p>For anyone wanting to get more involved in the life of the church there are many ways to do this and we ask everyone who counts Bright Path Church as home to have a ministry in some way, shape and form.</p>
      <p>Here is a list of just some of the ministries that take place on and outside of a Sunday at Bright Path Church that people can consider getting involved with when the time is right:</p>
    </div>
    <div class="strip" role="img" aria-label="Row of five photographs showing church ministry activities">
      <div></div><div></div><div></div><div></div><div></div>
    </div>
    <ul class="ministries">
      <li>Welcome Team</li><li>Pastoral Team</li>
      <li>Tech Team</li><li>Men's &amp; Women's Ministry</li>
      <li>Worship Team</li><li>Church Building &amp; Garden Maintenance</li>
      <li>Refreshments Team</li><li>Monday Night Football</li>
      <li>Kids Club (8-10s)</li><li>Quiz Nights</li>
      <li>Youth Club (11-14s)</li><li>Faith Questions Course</li>
      <li>Set Up Team</li><li>Movie Mornings</li>
      <li>Ministry Team</li><li>Little Tots</li>
    </ul>
    <div class="body-copy" style="left:40px;top:580px;width:460px">
      <p>For further details please see our website and social media page or speak to Daniel, Hannah or one of the leadership team to find out more.</p>
    </div>
    <svg class="wave" style="bottom:0" width="540" height="90" viewBox="0 0 540 90" aria-hidden="true">
      <path d="M0 40 C180 0 360 90 540 30 L540 90 L0 90Z" fill="var(--purple)"/>
      <path d="M0 70 C200 40 360 100 540 60 L540 90 L0 90Z" fill="var(--blue)"/>
    </svg>
  </article>
</section>

<!-- LETTER -->
<section class="page letter">
  <h2>KEEPING <span>IN TOUCH!</span></h2>
  <div class="body-copy">
    <p>Thank you so much for visiting Bright Path Church today. We would love to stay in touch with you and let you know about what is coming up in the life of our church family.</p>
    <p>If you would like to hear from us, please fill in the short form below and hand it to one of our welcome team, or simply pop it in the box at the back of the hall on your way out.</p>
    <p>We promise to keep your details safe and only use them to share news, events and invitations from Bright Path Church. You can ask us to stop at any time.</p>
    <p>We look forward to seeing you again soon,</p>
    <p><em class="sign">Daniel</em></p>
  </div>
  <div class="form">
    <h3>Your details</h3>
    <div class="field"><span>Name</span><i></i></div>
    <div class="field"><span>Address</span><i></i></div>
    <div class="field"><span></span><i></i></div>
    <div class="field"><span>Phone</span><i></i></div>
    <div class="field"><span>Email</span><i></i></div>
    <div class="checks">
      <label><b></b>Connect Groups</label>
      <label><b></b>Membership</label>
      <label><b></b>Ministries</label>
    </div>
  </div>
  <svg class="wave" style="bottom:0" width="740" height="90" viewBox="0 0 740 90" aria-hidden="true">
    <path d="M0 40 C240 90 480 0 740 45 L740 90 L0 90Z" fill="var(--sky)"/>
    <path d="M0 70 C260 100 480 50 740 72 L740 90 L0 90Z" fill="var(--purple)"/>
  </svg>
</section>

</body>
</html>
```